We need a design for our security installation based business. Our name is K M Security Systems

We need a business card for a security installation based company. We want to look modern and professional. We would like our company logo used and the three main colours to be white, black and orange. We install intruder alarms, cctv and access control. Our preference would be to use the black/orange design on the front and orange/black on the back. Feel free to post variations.

Target Market(s)

Business owners, commercial property and large residential properties

Industry/Entity Type

Business

Contact Information for Business Card

Owen Pelham 07813 592 640

Liam Fenwick 07751 286 419

operations@kmsecuritysystems.co.uk

Intruder Alarms
CCTV
Access Control

Colors
f78f20
000000
ffffff

Requirements
Must have
• Must have the logo on the business card somewhere

```html
<!DOCTYPE html>
<html lang="en">
<head>
<meta charset="utf-8">
<title>K M Security Systems – Business Card</title>
<link rel="stylesheet" href="https://fonts.googleapis.com/css2?family=Roboto+Condensed:wght@400;700&display=swap">
<style>
  :root {
    --backdrop: #2e2822;
    --card: #1c1d1e;
    --orange: #f05a22;
    --white: #f2f2f2;
    --grey: #d8d8d8;
  }
  * { margin: 0; padding: 0; box-sizing: border-box; }
  html, body {
    width: 1200px; height: 911px; overflow: hidden;
    background: var(--backdrop);
    font-family: "Roboto Condensed", "Arial Narrow", sans-serif;
  }
  .canvas { position: relative; width: 1200px; height: 911px; }
  .card {
    position: absolute;
    width: 500px; height: 286px;
    background: var(--card);
    box-shadow: 0 10px 30px rgba(0,0,0,0.45);
  }
  .card--contact { left: 70px; top: 312px; }
  .card--brand { left: 630px; top: 312px; }

  .contact-block { position: absolute; left: 40px; bottom: 34px; }
  .person { margin-bottom: 8px; }
  .person__name {
    color: var(--orange); font-weight: 700; font-size: 21px;
    text-transform: uppercase; letter-spacing: 0.2px; line-height: 1.1;
  }
  .person__phone { color: var(--grey); font-size: 15px; line-height: 1.3; }
  .company-links { margin-top: 8px; }
  .company-links__item {
    color: var(--white); font-size: 14px; text-transform: uppercase;
    line-height: 1.35; letter-spacing: 0.2px;
  }

  .brand {
    position: absolute; left: 0; right: 0; top: 100px;
    display: flex; align-items: center; justify-content: center; gap: 12px;
  }
  .brand__mark {
    width: 12px; height: 12px; border-radius: 50%; background: var(--orange);
  }
  .brand__name {
    color: var(--white); font-weight: 400; font-size: 30px;
    letter-spacing: 0.3px;
  }
  .services {
    position: absolute; left: 0; right: 0; top: 166px;
    text-align: center; color: var(--white); font-size: 15px; letter-spacing: 0.2px;
  }
  .services__dot { color: var(--orange); margin: 0 6px; }
</style>
</head>
<body>
<main class="canvas">
  <section class="card card--contact" aria-label="Business card reverse">
    <div class="contact-block">
      <div class="person">
        <p class="person__name">Owen Pelham</p>
        <p class="person__phone">07813 592 640</p>
      </div>
      <div class="person">
        <p class="person__name">Liam Fenwick</p>
        <p class="person__phone">07751 286 419</p>
      </div>
      <div class="company-links">
        <p class="company-links__item">operations@kmsecuritysystems.co.uk</p>
        <p class="company-links__item">www.kmsecuritysystems.co.uk</p>
      </div>
    </div>
  </section>

  <section class="card card--brand" aria-label="Business card front">
    <div class="brand">
      <span class="brand__mark" aria-hidden="true"></span>
      <span class="brand__name">K M Security Systems</span>
    </div>
    <p class="services">Intruder Alarms<span class="services__dot">•</span>CCTV<span class="services__dot">•</span>Access Control</p>
  </section>
</main>
</body>
</html>
```